Medical Simulation - Creative Graphic for Data

My company needs a creative graph that depicts the rationales (or reasons) our learners chose certain drug options. Basically, our clients not only want to know how many times certain drugs were selected, but the "whys" behind their choices. I would like a PPT graphic that I can use for other deliverables, where I can simply switch out the drug (treatment) names, the "whys" (what we call rationales), and the specific metrics (percentages, "n" numbers, etc), and the graphic will update and adjust to the new information. The title of the graph (or the slide where the graph will live) should be something like "Treatment Rationales" or something to that effect. Include a placeholder for text to go if anyone wants to add an analysis of the graphic later. This placeholder should accommodate 2-3 bullet points of text. We want this graphic to not just be an image, but organized in a way that you would see in a presentation slide, with a title, place holder for analysis (as indicated above), branding colors, and helpful information to understand the graphic (what is included in this post and it's associated attachments).

I've included specific drug names, rationales, and metrics to use for this (please see excel document). If you are going to design the graph directly in PPT, please use the PPT template design included. Please don't feel like you have to use 1 slide only or can have multiple graphs, if that makes sense for you design idea. They just need to fit within the coloring of the PPT. For font, please use Arial. Below is a Google Drive Link to branding colors and vector art.

https://files.plorvex.net/open?id=7QkR2mTw8-LpXa04vNbHcY3TnpRd

We are open to many variations and design ideas. Please don't feel like you have to limit yourself! I've attached a few ideas that we've had and it may be a good place to start. We would ESPECIALLY like to see a version utilizing the radial graph (similar to the one included in the Rationales_DesignIdeas document).

Please reach out if you have any questions. Thanks!

Industry/Entity Type

Drug

Requirements
Nice to have
• It would be great to see the radial graph as a design variation (see link below)
• http://4.vistragrid.net/products/vistragrid/docs/users-guide/img/Samples/radar-chart-fixed-radius.png

```html
<!DOCTYPE html>
<html lang="en">
<head>
<meta charset="utf-8">
<title>Rationale Data</title>
<link rel="stylesheet" href="https://fonts.googleapis.com/css2?family=Arimo:wght@400;700&display=swap">
<style>
  :root{
    --navy:#0d4261;
    --title:#0f4a6d;
    --seg-dark:#12334f;
    --seg-blue:#4a80c4;
    --seg-gray:#939598;
    --seg-light:#dcdddf;
    --orange:#f5954a;
    --text:#444;
    --page:#ececec;
  }
  *{box-sizing:border-box;margin:0;padding:0}
  html,body{width:1200px;height:1200px;overflow:hidden}
  body{background:var(--page);font-family:Arimo,Arial,sans-serif;position:relative}
  .slide{position:absolute;left:40px;top:180px;width:1400px;height:1050px;background:#fff;transform:scale(.8);transform-origin:0 0;overflow:hidden}
  .top-band{position:absolute;left:0;top:0;width:100%;height:33px;background:var(--navy)}
  .brand-strip{position:absolute;right:0;top:33px;width:340px;height:35px;background:linear-gradient(90deg,rgba(245,149,74,0) 0%,rgba(245,149,74,.55) 35%,var(--orange) 100%);}
  .brand-strip span{position:absolute;right:28px;top:5px;color:#fff;font-weight:700;font-size:22px;line-height:25px}
  .rule{position:absolute;left:0;width:1000px;height:10px;background:linear-gradient(180deg,rgba(0,0,0,.07),rgba(0,0,0,0));}
  .rule-top{top:60px}
  .rule-bottom{top:210px}
  .title{position:absolute;left:85px;top:106px;font-size:45px;font-weight:700;color:var(--title)}
  .chart{position:absolute;left:0;top:0;width:1400px;height:1050px}
  .seg{fill:none;stroke-width:30}
  .dark{stroke:var(--seg-dark)} .blue{stroke:var(--seg-blue)} .gray{stroke:var(--seg-gray)} .light{stroke:var(--seg-light)}
  .pill rect{filter:drop-shadow(1px 2px 1.5px rgba(0,0,0,.3))}
  .pill text{font-size:11px;fill:#fff;text-anchor:middle;dominant-baseline:central;font-family:Arimo,Arial,sans-serif}
  .p-dark rect{fill:var(--seg-dark)} .p-blue rect{fill:var(--seg-blue)} .p-gray rect{fill:var(--seg-gray)} .p-light rect{fill:var(--seg-light)}
  .tag{position:absolute;height:29px;color:#fff;font-weight:700;font-size:19px;line-height:29px}
  .tag-treatment{left:0;top:562px;width:175px;background:var(--orange);border-radius:0 15px 15px 0;padding-left:38px}
  .tag-rationales{right:0;top:800px;width:298px;height:34px;line-height:34px;background:var(--seg-dark);border-radius:17px 0 0 17px;padding-left:19px;font-size:20px}
  .treatments{position:absolute;left:38px;top:607px;width:753px;list-style:none}
  .treatment{display:flex;align-items:center;height:44.7px;font-size:16px;color:var(--text)}
  .treatment .name{white-space:nowrap}
  .treatment .leader{flex:1;height:4px;margin:0 2px 0 5px;background:repeating-linear-gradient(90deg,var(--orange) 0 4px,transparent 4px 7px)}
  .treatment .dot{width:12px;height:12px;border-radius:50%;background:var(--orange);margin-right:11px}
  .treatment .bar{height:31px;background:var(--orange);color:#fff;font-size:16px;text-align:right;padding-right:13px;line-height:31px}
  .legend{position:absolute;left:1110px;top:845px;list-style:none;font-size:15px;color:var(--text);line-height:19px}
  .legend li{display:flex;align-items:flex-start;gap:9px}
  .legend .sw{width:14px;height:14px;margin-top:2px;flex:none}
  .sw.dark{background:var(--seg-dark)} .sw.blue{background:var(--seg-blue)} .sw.gray{background:var(--seg-gray)} .sw.light{background:var(--seg-light)}
  .notes{position:absolute;left:52px;top:966px;font-size:12.5px;line-height:17px}
  .notes .n1{color:var(--orange)} .notes .n2{color:#222}
  .footer{position:absolute;left:0;bottom:0;width:100%;height:31px;background:var(--navy);color:#fff;text-align:center;font-size:15px;line-height:31px}
</style>
</head>
<body>
<main class="slide">
  <div class="top-band"></div>
  <div class="brand-strip"><span>Clinora</span></div>
  <div class="rule rule-top"></div>
  <h1 class="title">Rationale Data</h1>
  <div class="rule rule-bottom"></div>

  <svg class="chart" viewBox="50 225 1400 1050" role="img" aria-label="Radial chart of rationale shares per treatment">
    <g transform="translate(848 810) scale(-1 1) rotate(90)">
      <circle class="seg blue"  r="37" pathLength="150" stroke-dasharray="50 150"/>
      <circle class="seg light" r="37" pathLength="150" stroke-dasharray="50 150" stroke-dashoffset="-50"/>
      <circle class="seg dark"  r="82" pathLength="150" stroke-dasharray="50 150"/>
      <circle class="seg blue"  r="82" pathLength="150" stroke-dasharray="50 150" stroke-dashoffset="-50"/>
      <circle class="seg gray"  r="126" pathLength="150" stroke-dasharray="50 150"/>
      <circle class="seg light" r="126" pathLength="150" stroke-dasharray="50 150" stroke-dashoffset="-50"/>
      <circle class="seg dark"  r="171" pathLength="150" stroke-dasharray="8 150"/>
      <circle class="seg blue"  r="171" pathLength="150" stroke-dasharray="8 150" stroke-dashoffset="-8"/>
      <circle class="seg gray"  r="171" pathLength="150" stroke-dasharray="42 150" stroke-dashoffset="-16"/>
      <circle class="seg light" r="171" pathLength="150" stroke-dasharray="42 150" stroke-dashoffset="-58"/>
      <circle class="seg dark"  r="216" pathLength="150" stroke-dasharray="19 150"/>
      <circle class="seg blue"  r="216" pathLength="150" stroke-dasharray="17 150" stroke-dashoffset="-19"/>
      <circle class="seg gray"  r="216" pathLength="150" stroke-dasharray="26 150" stroke-dashoffset="-36"/>
      <circle class="seg light" r="216" pathLength="150" stroke-dasharray="38 150" stroke-dashoffset="-62"/>
      <circle class="seg dark"  r="261" pathLength="150" stroke-dasharray="49 150"/>
      <circle class="seg blue"  r="261" pathLength="150" stroke-dasharray="17 150" stroke-dashoffset="-49"/>
      <circle class="seg gray"  r="261" pathLength="150" stroke-dasharray="17 150" stroke-dashoffset="-66"/>
      <circle class="seg light" r="261" pathLength="150" stroke-dasharray="17 150" stroke-dashoffset="-83"/>
      <circle class="seg dark"  r="306" pathLength="150" stroke-dasharray="18 150"/>
      <circle class="seg blue"  r="306" pathLength="150" stroke-dasharray="36 150" stroke-dashoffset="-18"/>
      <circle class="seg gray"  r="306" pathLength="150" stroke-dasharray="18 150" stroke-dashoffset="-54"/>
      <circle class="seg light" r="306" pathLength="150" stroke-dasharray="28 150" stroke-dashoffset="-72"/>
    </g>
    <g class="labels">
      <g class="pill p-light" transform="translate(713 537)"><rect x="-20" y="-11" width="40" height="22" rx="11"/><text>27%</text></g>
      <g class="pill p-gray"  transform="translate(993 540)"><rect x="-20" y="-11" width="40" height="22" rx="11"/><text>18%</text></g>
      <g class="pill p-blue"  transform="translate(1155 826)"><rect x="-20" y="-11" width="40" height="22" rx="11"/><text>36%</text></g>
      <g class="pill p-dark"  transform="translate(963 1094)"><rect x="-20" y="-11" width="40" height="22" rx="11"/><text>18%</text></g>
      <g class="pill p-light" transform="translate(681 609)"><rect x="-20" y="-11" width="40" height="22" rx="11"/><text>17%</text></g>
      <g class="pill p-gray"  transform="translate(849 548)"><rect x="-20" y="-11" width="40" height="22" rx="11"/><text>17%</text></g>
      <g class="pill p-blue"  transform="translate(1017 609)"><rect x="-20" y="-11" width="40" height="22" rx="11"/><text>17%</text></g>
      <g class="pill p-dark"  transform="translate(1075 940)"><rect x="-20" y="-11" width="40" height="22" rx="11"/><text>50%</text></g>
      <g class="pill p-light" transform="translate(795 600)"><rect x="-20" y="-11" width="40" height="22" rx="11"/><text>38%</text></g>
      <g class="pill p-gray"  transform="translate(1041 709)"><rect x="-20" y="-11" width="40" height="22" rx="11"/><text>26%</text></g>
      <g class="pill p-blue"  transform="translate(1047 898)"><rect x="-20" y="-11" width="40" height="22" rx="11"/><text>17%</text></g>
      <g class="pill p-dark"  transform="translate(933 1011)"><rect x="-20" y="-11" width="40" height="22" rx="11"/><text>19%</text></g>
      <g class="pill p-light" transform="translate(820 640)"><rect x="-20" y="-11" width="40" height="22" rx="11"/><text>42%</text></g>
      <g class="pill p-gray"  transform="translate(1020 813)"><rect x="-20" y="-11" width="40" height="22" rx="11"/><text>42%</text></g>
      <g class="pill p-blue"  transform="translate(931 961)"><rect x="-18" y="-11" width="36" height="22" rx="11"/><text>8%</text></g>
      <g class="pill p-dark"  transform="translate(877 980)"><rect x="-18" y="-11" width="36" height="22" rx="11"/><text>8%</text></g>
      <g class="pill p-light" transform="translate(849 680)"><rect x="-20" y="-11" width="40" height="22" rx="11"/><text>50%</text></g>
      <g class="pill p-gray"  transform="translate(960 872)"><rect x="-20" y="-11" width="40" height="22" rx="11"/><text>50%</text></g>
      <g class="pill p-blue"  transform="translate(848 723)"><rect x="-20" y="-11" width="40" height="22" rx="11"/><text>50%</text></g>
      <g class="pill p-dark"  transform="translate(922 851)"><rect x="-20" y="-11" width="40" height="22" rx="11"/><text>50%</text></g>
      <g class="pill p-light" transform="translate(849 767)"><rect x="-20" y="-11" width="40" height="22" rx="11"/><text>50%</text></g>
      <g class="pill p-blue"  transform="translate(885 828)"><rect x="-20" y="-11" width="40" height="22" rx="11"/><text>50%</text></g>
    </g>
  </svg>

  <div class="tag tag-treatment">Treatment*</div>
  <ul class="treatments">
    <li class="treatment"><span class="name">irinotecan</span><span class="leader"></span><span class="dot"></span><span class="bar" style="width:70px">n = 20</span></li>
    <li class="treatment"><span class="name">irinotecan/leucovorin/5-FU plus cetuximab</span><span class="leader"></span><span class="dot"></span><span class="bar" style="width:105px">n = 30</span></li>
    <li class="treatment"><span class="name">oxaliplatin/leucovorin/5-FU</span><span class="leader"></span><span class="dot"></span><span class="bar" style="width:105px">n = 30</span></li>
    <li class="treatment"><span class="name">oxaliplatin/capecitabine plus bevacizumab</span><span class="leader"></span><span class="dot"></span><span class="bar" style="width:176px">n = 50</span></li>
    <li class="treatment"><span class="name">oxaliplatin/leucovorin/5-FU plus bevacizumab</span><span class="leader"></span><span class="dot"></span><span class="bar" style="width:176px">n = 50</span></li>
    <li class="treatment"><span class="name">oxaliplatin/capecitabine</span><span class="leader"></span><span class="dot"></span><span class="bar" style="width:246px">n = 70</span></li>
    <li class="treatment"><span class="name">irinotecan/leucovorin/5-FU plus bevacizumab</span><span class="leader"></span><span class="dot"></span><span class="bar" style="width:352px">n = 100</span></li>
  </ul>

  <div class="tag tag-rationales">Rationales*</div>
  <ul class="legend">
    <li><span class="sw dark"></span>Fewer overall side effects</li>
    <li><span class="sw blue"></span>Impact on quality of life</li>
    <li><span class="sw gray"></span>Preserves future treatment<br>options</li>
    <li><span class="sw light"></span>Recent guidelines</li>
  </ul>

  <div class="notes">
    <p class="n1">*Number of Drug Selections</p>
    <p class="n2">*Learners can select 1-2 rationales for each treatment ordered</p>
  </div>

  <footer class="footer">Clinora Education Confidential and Proprietary Information</footer>
</main>
</body>
</html>
```